Painting and decorating services

A flyer that promotes my services as a high quality painter and decorator. My services are fully flexible and we cater for range of customers from the decoration of small homes through to larger businesses. We have the flexibility to work through the night which suits businesses that cannot afford to shut throughout the day. We guarantee a top quality finish and are proud to promote a loyalty scheme for successful referrals.

We are truly a family business that is proud and confident to offer one of the most reliable and friendly services on offer.

Target Market(s)

Family homes, businesses who want offer of 24/7 services

Industry/Entity Type

Painting

Font styles to use
Serif
Sans Serif

Requirements
Must have
• Promotion of reliability, value, quality, service
• Days rates and price work considered
• Promotion of night work
• Loyalty scheme / incentives offerred for referrals
• Concept that we are an extremely hard working team who work extended hours and offer flexibility to customers
• Some picture examples of high quality paint jobs as examples of my work.
• Contact details. Phone 01745382916 or mobile 0762931846 email: tkbrushandfinishworks@mailvane.com
Nice to have
• Notion of friendliness coming across from the advert.
• Commitment to giving the customer what they want and delivering to the highest specifications requested
Should not have
• Any over exaggerated false promises that would make the reader of the flyer believe it's just another blagging tradesman with false marketing and empty promises.

```html
<!DOCTYPE html>
<html lang="en">
<head>
<meta charset="utf-8">
<title>TK Brush &amp; Finish – Painting and Decorating Flyer</title>
<link href="https://fonts.googleapis.com/css2?family=Montserrat:wght@500;600&family=Oswald:wght@500&family=Signika:wght@400&family=Open+Sans:ital,wght@0,400;1,400&display=swap" rel="stylesheet">
<style>
  :root{
    --page-bg:#e6e6e6;
    --brand-blue:#3f5eab;
    --sky:#5cc3ec;
    --paper:#f2f2f3;
    --list-text:#1f4f8f;
    --review-text:#555b63;
    --white:#ffffff;
    --gold:#f2b417;
  }
  *{box-sizing:border-box;margin:0;padding:0}
  html,body{width:931px;height:1200px;overflow:hidden;background:var(--page-bg)}
  .flyer{
    position:absolute;left:63px;top:28px;width:700px;height:994px;
    transform:scale(1.15);transform-origin:top left;
    background:var(--paper);overflow:hidden;
    box-shadow:0 4px 14px rgba(0,0,0,.25);
  }
  .hero{position:absolute;left:0;top:0;width:700px;height:520px}
  .brand-name{
    position:absolute;left:28px;top:42px;white-space:nowrap;
    font:600 24px/1 "Montserrat",sans-serif;color:var(--white);
  }
  .tagline{
    position:absolute;right:28px;top:34px;
    font:500 21.5px/1 "Montserrat",sans-serif;color:var(--white);letter-spacing:.3px;
  }
  .work-samples{position:absolute;left:537px;top:0}
  .sample{
    position:absolute;left:0;width:140px;height:140px;border-radius:50%;
    border:5px solid var(--white);
    box-shadow:0 3px 8px rgba(0,0,0,.35);
  }
  .sample--roof{top:345px;background:radial-gradient(circle at 35% 30%,#eeeeee,#8c8f94)}
  .sample--door{top:487px;background:radial-gradient(circle at 35% 30%,#c98b72,#8a5a4a)}
  .sample--house{top:624px;background:radial-gradient(circle at 35% 30%,#e6e8ea,#9aa4ae)}
  .sample--van{top:750px;background:radial-gradient(circle at 35% 30%,#6f8fd2,#35539e)}
  .services-tab{
    position:absolute;left:0;top:492px;width:372px;height:64px;
    background:var(--brand-blue);border-radius:0 32px 32px 0;
    box-shadow:0 3px 5px rgba(0,0,0,.25);
    font:500 25px/64px "Oswald",sans-serif;color:var(--white);padding-left:28px;
  }
  .service-list{position:absolute;left:20px;top:580px;list-style:none}
  .service-list li{
    display:flex;align-items:center;height:36.7px;
    font:400 20.5px/1 "Signika",sans-serif;color:var(--list-text);
  }
  .service-list svg{width:19px;height:19px;margin-right:13px;flex:none}
  .review{position:absolute;left:22px;top:810px;width:480px}
  .review-head{display:flex;align-items:center;gap:3px;font:400 14px/1 "Open Sans",sans-serif;color:var(--review-text)}
  .review-head span{margin-left:8px}
  .review-head svg{width:13px;height:13px}
  .review-text{margin-top:6px;font:italic 400 13.5px/20px "Open Sans",sans-serif;color:var(--review-text)}
  .contact-bar{
    position:absolute;left:0;top:908px;width:700px;height:86px;background:var(--brand-blue);
    color:var(--white);text-align:center;
  }
  .contact-line{display:flex;justify-content:center;align-items:center;gap:12px;margin-top:18px;
    font:500 27px/1 "Oswald",sans-serif}
  .contact-line svg{width:30px;height:30px}
  .contact-email{margin-top:10px;font:500 13.5px/1 "Montserrat",sans-serif;letter-spacing:1px}
</style>
</head>
<body>
<div class="flyer">
  <svg class="hero" viewBox="0 0 700 520">
    <defs>
      <linearGradient id="interior" x1="0" y1="0" x2="1" y2="1">
        <stop offset="0" stop-color="#d9d5cf"/>
        <stop offset=".5" stop-color="#eeeeee"/>
        <stop offset="1" stop-color="#b9b3ad"/>
      </linearGradient>
    </defs>
    <rect width="700" height="300" fill="var(--brand-blue)"/>
    <path d="M0,252 Q330,90 700,100 L700,112 Q340,104 0,268 Z" fill="var(--sky)"/>
    <path d="M0,268 Q340,104 700,112 L700,118 Q345,112 0,272 Z" fill="var(--white)"/>
    <path d="M0,272 Q345,112 700,118 L700,520 L0,520 Z" fill="url(#interior)" role="img" aria-label="Photo of a freshly decorated bright living room and open kitchen"/>
    <path d="M0,478 Q330,410 700,432 L700,520 L0,520 Z" fill="var(--paper)"/>
    <path d="M0,470 Q330,400 700,418 L700,432 Q330,414 0,484 Z" fill="var(--brand-blue)"/>
    <path d="M0,486 Q330,424 700,440 L700,446 Q330,432 0,492 Z" fill="var(--sky)"/>
  </svg>
  <div class="brand-name">TK Brush &amp; Finish</div>
  <div class="tagline">PAINTING AND DECORATING</div>

  <div class="services-tab">FAMILY, FRIENDLY SERVICES</div>
  <ul class="service-list">
    <li><svg viewBox="0 0 20 20"><circle cx="10" cy="10" r="10" fill="var(--sky)"/><path d="M8 5.5l4.5 4.5L8 14.5" stroke="#fff" stroke-width="2.4" fill="none"/></svg>Reliability, Value, Quality, Service</li>
    <li><svg viewBox="0 0 20 20"><circle cx="10" cy="10" r="10" fill="var(--sky)"/><path d="M8 5.5l4.5 4.5L8 14.5" stroke="#fff" stroke-width="2.4" fill="none"/></svg>Days Rates And Price Work Considered</li>
    <li><svg viewBox="0 0 20 20"><circle cx="10" cy="10" r="10" fill="var(--sky)"/><path d="M8 5.5l4.5 4.5L8 14.5" stroke="#fff" stroke-width="2.4" fill="none"/></svg>Flexibility To Work Through The Night</li>
    <li><svg viewBox="0 0 20 20"><circle cx="10" cy="10" r="10" fill="var(--sky)"/><path d="M8 5.5l4.5 4.5L8 14.5" stroke="#fff" stroke-width="2.4" fill="none"/></svg>Loyalty Scheme / Incentives Offerred For Referrals</li>
    <li><svg viewBox="0 0 20 20"><circle cx="10" cy="10" r="10" fill="var(--sky)"/><path d="M8 5.5l4.5 4.5L8 14.5" stroke="#fff" stroke-width="2.4" fill="none"/></svg>Hard Working Team Who Work Extended Hours</li>
    <li><svg viewBox="0 0 20 20"><circle cx="10" cy="10" r="10" fill="var(--sky)"/><path d="M8 5.5l4.5 4.5L8 14.5" stroke="#fff" stroke-width="2.4" fill="none"/></svg>Flexibility To Customers</li>
  </ul>

  <div class="review">
    <div class="review-head">
      <svg viewBox="0 0 20 20"><path d="M10 1l2.6 6 6.4.5-4.9 4.2 1.5 6.3L10 14.6 4.4 18l1.5-6.3L1 7.5 7.4 7z" fill="var(--gold)"/></svg>
      <svg viewBox="0 0 20 20"><path d="M10 1l2.6 6 6.4.5-4.9 4.2 1.5 6.3L10 14.6 4.4 18l1.5-6.3L1 7.5 7.4 7z" fill="var(--gold)"/></svg>
      <svg viewBox="0 0 20 20"><path d="M10 1l2.6 6 6.4.5-4.9 4.2 1.5 6.3L10 14.6 4.4 18l1.5-6.3L1 7.5 7.4 7z" fill="var(--gold)"/></svg>
      <svg viewBox="0 0 20 20"><path d="M10 1l2.6 6 6.4.5-4.9 4.2 1.5 6.3L10 14.6 4.4 18l1.5-6.3L1 7.5 7.4 7z" fill="var(--gold)"/></svg>
      <svg viewBox="0 0 20 20"><path d="M10 1l2.6 6 6.4.5-4.9 4.2 1.5 6.3L10 14.6 4.4 18l1.5-6.3L1 7.5 7.4 7z" fill="var(--gold)"/></svg>
      <span>Maya</span>
    </div>
    <p class="review-text">Tom is an amazing decorator! he painted my kitchen and did a perfect job. getting him back to do my living room and dining room! would highly recommend !</p>
  </div>

  <div class="work-samples">
    <div class="sample sample--roof" role="img" aria-label="Photo of a painted roofline and fascia"></div>
    <div class="sample sample--door" role="img" aria-label="Photo of a painted front door"></div>
    <div class="sample sample--house" role="img" aria-label="Photo of a freshly painted house exterior"></div>
    <div class="sample sample--van" role="img" aria-label="Photo of the company work van"></div>
  </div>

  <div class="contact-bar">
    <div class="contact-line">
      <span>CONTACT US TODAY</span>
      <svg viewBox="0 0 30 30"><circle cx="15" cy="15" r="13" fill="none" stroke="#fff" stroke-width="2"/><path d="M10.5 8.5l2.5-.5 1.5 3.5-1.8 1.2a8 8 0 004.1 4.1l1.2-1.8 3.5 1.5-.5 2.5c-6 .8-11.3-4.5-10.5-10.5z" fill="#fff"/></svg>
      <span>01745382916&nbsp;&nbsp;|&nbsp;&nbsp;0762931846</span>
    </div>
    <div class="contact-email">tkbrushandfinishworks@mailvane.com</div>
  </div>
</div>
</body>
</html>
```